A Clear Three Step Roadmap For Contractors

We are looking for a one-pager "roadmap" that is similar to the 2nd picture we attached, but much more professional & better... please make it landscape orientation. The logo for this system is attached below, as well.

Our Brand Colors to use:
#f2d582
#303030
#8b8c90

The copy we'd like to use on the flyer:
A Clear Three Step Roadmap that will finally allow you to attract quality customers and win more jobs.

The Keystone Ladder Method is a simple to follow system that was created specifically for Contractors and Blue Collar Business Owners.

When it comes to marketing and growing their business, the majority of Contractors are left confused, frustrated and extremely overwhelmed. Unlike most sales, marketing & training programs that offer a single "piece of the puzzle", we've mapped out each essential step of the puzzle and cut out all of the fluff.

All you have to do is complete each step in the right order and we'll be guiding you along the entire journey!

A ---> B

Blueprint: Get clear on where you're going, define your ideal audience, and finally, master your message.
Step 1: Clarify The Chaos
Step 2: Define Your Customer
Step 3: Master Your Message

Build: Attract quality leads, Build your funnel and Formulate a high-converting follow-up system
Step 4: Develop Lead Generator
Step 5: Construct Your Funnel
Step 6: Formulate the Follow-Up

Breakthrough: Get in front of your ideal customers and rapidly scale your business by driving traffic and becoming the authority in your market
Step 7: Turn-On the Traffic
Step 8: Become the Authority
Step 9: Unlock Your Growth

```html
<!DOCTYPE html>
<html lang="en">
<head>
<meta charset="utf-8">
<title>Keystone Ladder Method – Three Step Roadmap</title>
<link rel="stylesheet" href="https://fonts.googleapis.com/css2?family=Open+Sans:wght@300;400;600&family=Signika:wght@400;600;700&display=swap">
<style>
  :root {
    --gold: #f2d582;
    --gold-deep: #e2c15e;
    --charcoal: #303030;
    --slate: #8b8c90;
    --paper: #ffffff;
    --stage: #7a7a7a;
    --heading-font: "Signika", sans-serif;
    --body-font: "Open Sans", sans-serif;
  }
  html, body {
    margin: 0;
    padding: 0;
    width: 1200px;
    height: 904px;
    overflow: hidden;
    background: var(--stage);
  }
  .flyer {
    position: absolute;
    left: 40px;
    top: 137px;
    width: 1703px;
    height: 958px;
    transform: scale(0.6577);
    transform-origin: top left;
    background: var(--gold);
    overflow: hidden;
    font-family: var(--body-font);
    color: var(--charcoal);
  }
  .flyer-shapes { position: absolute; inset: 0; }
  .brand {
    position: absolute;
    left: 43px;
    top: 45px;
    display: flex;
    align-items: center;
    gap: 24px;
  }
  .brand-square { width: 104px; height: 104px; background: var(--gold); }
  .brand-name {
    font-family: var(--heading-font);
    font-weight: 700;
    font-size: 48px;
    line-height: 50px;
    color: var(--charcoal);
    text-transform: uppercase;
    letter-spacing: 0.5px;
  }
  .headline {
    position: absolute;
    left: 718px;
    top: 53px;
    width: 960px;
    margin: 0;
    font-family: var(--heading-font);
    font-weight: 700;
    font-size: 38px;
    line-height: 46px;
    color: var(--charcoal);
  }
  .intro {
    position: absolute;
    left: 43px;
    top: 234px;
    width: 578px;
    color: #ffffff;
    font-size: 17.4px;
    line-height: 21.5px;
    font-weight: 300;
    text-align: justify;
  }
  .intro p { margin: 0 0 21px; }
  .intro .intro-cta { font-weight: 400; margin-top: 26px; }
  .phase-list {
    position: absolute;
    left: 43px;
    top: 531px;
    width: 578px;
    margin: 0;
    padding: 0;
    list-style: none;
  }
  .phase {
    position: relative;
    padding-left: 99px;
    min-height: 90px;
    margin-bottom: 24px;
  }
  .phase-number {
    position: absolute;
    left: 0;
    top: 0;
    width: 74px;
    height: 74px;
    border: 4px solid var(--charcoal);
    border-radius: 50%;
    display: flex;
    align-items: center;
    justify-content: center;
    font-size: 52px;
    font-weight: 400;
    line-height: 1;
  }
  .phase-title {
    margin: 8px 0 3px;
    font-family: var(--heading-font);
    font-weight: 700;
    font-size: 31px;
    line-height: 32px;
  }
  .phase-text {
    margin: 0;
    font-size: 17px;
    line-height: 21.5px;
    font-weight: 600;
    text-align: justify;
  }
  .roadmap text { font-family: var(--heading-font); }
  .step-label { fill: var(--gold); font-size: 14.5px; font-weight: 600; text-anchor: middle; }
  .tier-label { fill: #ffffff; font-size: 21px; font-weight: 600; }
  .tier-digit { fill: var(--charcoal); font-size: 21px; font-family: var(--body-font); text-anchor: middle; }
  .endpoint { fill: var(--gold); font-size: 40px; font-weight: 700; }
  .path-line { stroke: #9a9a9a; stroke-width: 2; stroke-dasharray: 7 5; fill: none; }
  .icon-disc { fill: #ffffff; }
</style>
</head>
<body>
<main class="flyer">
  <svg class="flyer-shapes" width="1703" height="958" viewBox="0 0 1703 958">
    <defs>
      <linearGradient id="darkBand" x1="0" y1="0" x2="1" y2="1">
        <stop offset="0" stop-color="#2b2b2b"/>
        <stop offset="0.5" stop-color="#363636"/>
        <stop offset="1" stop-color="#2a2a2a"/>
      </linearGradient>
      <linearGradient id="deviceTone" x1="0" y1="0" x2="0" y2="1">
        <stop offset="0" stop-color="#d9d9db"/>
        <stop offset="1" stop-color="#a9a9ab"/>
      </linearGradient>
      <linearGradient id="display" x1="0" y1="0" x2="1" y2="1">
        <stop offset="0" stop-color="#262626"/>
        <stop offset="0.55" stop-color="#333333"/>
        <stop offset="1" stop-color="#242424"/>
      </linearGradient>
    </defs>

    <rect x="0" y="183" width="1703" height="324" fill="url(#darkBand)"/>
    <rect x="0" y="0" width="1703" height="183" fill="var(--gold)"/>
    <polygon points="0,0 680,0 620,183 0,183" fill="var(--paper)"/>
    <polygon points="680,0 702,0 642,183 620,183" fill="var(--charcoal)"/>

    <!-- device frame area: flat tones only -->
    <g role="img" aria-label="Laptop device frame holding the roadmap screen">
      <rect x="680" y="253" width="890" height="600" rx="22" fill="#1a1a1a" stroke="#d9d9db" stroke-width="4"/>
      <rect x="593" y="851" width="1067" height="64" rx="22" fill="url(#deviceTone)"/>
    </g>
    <rect x="712" y="291" width="826" height="518" fill="url(#display)"/>

    <g class="roadmap">
      <path class="path-line" d="M1026 719 H1153 M1241 719 H1364 M1408 675 V594 M1026 550 H1153 M1241 550 H1364 M982 506 V436 M1026 392 H1153 M1241 392 H1364"/>

      <circle class="icon-disc" cx="982" cy="719" r="45"/>
      <circle class="icon-disc" cx="1197" cy="719" r="44"/>
      <circle class="icon-disc" cx="1408" cy="719" r="44"/>
      <circle class="icon-disc" cx="982" cy="550" r="44"/>
      <circle class="icon-disc" cx="1197" cy="550" r="44"/>
      <circle class="icon-disc" cx="1408" cy="550" r="44"/>
      <circle class="icon-disc" cx="982" cy="392" r="44"/>
      <circle class="icon-disc" cx="1197" cy="392" r="44"/>
      <circle class="icon-disc" cx="1408" cy="392" r="44"/>

      <!-- target -->
      <g class="icon icon-target">
        <circle cx="982" cy="719" r="34" fill="var(--gold)" stroke="var(--charcoal)" stroke-width="3"/>
        <circle cx="982" cy="719" r="17" fill="none" stroke="var(--charcoal)" stroke-width="3"/>
        <path d="M982 694 V744 M957 719 H1007" stroke="var(--charcoal)" stroke-width="3"/>
      </g>
      <!-- customer (plain user shape) -->
      <g class="icon icon-user">
        <circle cx="1197" cy="702" r="14" fill="var(--gold)"/>
        <path d="M1170 748 Q1170 720 1197 720 Q1224 720 1224 748 Z" fill="var(--gold)"/>
        <path d="M1193 722 H1201 L1203 744 L1197 750 L1191 744 Z" fill="var(--charcoal)"/>
      </g>
      <!-- megaphone -->
      <g class="icon icon-megaphone">
        <polygon points="1384,708 1418,690 1418,748 1384,730" fill="var(--gold)"/>
        <rect x="1376" y="706" width="12" height="26" rx="3" fill="var(--gold-deep)"/>
        <rect x="1418" y="686" width="8" height="66" rx="3" fill="var(--charcoal)"/>
        <rect x="1386" y="730" width="9" height="20" fill="var(--slate)"/>
      </g>
      <!-- servers with arrow -->
      <g class="icon icon-servers">
        <rect x="956" y="526" width="52" height="13" rx="4" fill="#e6e6e6" stroke="var(--slate)" stroke-width="2"/>
        <rect x="956" y="544" width="52" height="13" rx="4" fill="#e6e6e6" stroke="var(--slate)" stroke-width="2"/>
        <rect x="956" y="562" width="52" height="13" rx="4" fill="#e6e6e6" stroke="var(--slate)" stroke-width="2"/>
        <circle cx="963" cy="532" r="2.5" fill="var(--charcoal)"/>
        <circle cx="963" cy="550" r="2.5" fill="var(--charcoal)"/>
        <circle cx="963" cy="568" r="2.5" fill="var(--charcoal)"/>
        <polygon points="982,522 996,538 988,538 988,566 976,566 976,538 968,538" fill="var(--gold)" stroke="var(--charcoal)" stroke-width="1.5"/>
      </g>
      <!-- funnel -->
      <g class="icon icon-funnel">
        <circle cx="1186" cy="521" r="2.5" fill="var(--charcoal)"/>
        <circle cx="1197" cy="516" r="2.5" fill="var(--charcoal)"/>
        <circle cx="1208" cy="522" r="2.5" fill="var(--charcoal)"/>
        <rect x="1170" y="530" width="54" height="7" fill="var(--gold)"/>
        <polygon points="1170,537 1224,537 1204,560 1204,580 1190,574 1190,560" fill="var(--slate)"/>
      </g>
      <!-- magnet -->
      <g class="icon icon-magnet">
        <path d="M1392 532 V556 A16 16 0 0 0 1424 556 V532" fill="none" stroke="var(--gold)" stroke-width="12"/>
        <rect x="1386" y="524" width="12" height="10" fill="var(--charcoal)"/>
        <rect x="1418" y="524" width="12" height="10" fill="var(--charcoal)"/>
      </g>
      <!-- browser window -->
      <g class="icon icon-browser">
        <rect x="956" y="368" width="52" height="46" rx="3" fill="#f2f2f2" stroke="var(--charcoal)" stroke-width="2.5"/>
        <rect x="956" y="368" width="52" height="8" fill="var(--charcoal)"/>
        <rect x="962" y="382" width="16" height="12" fill="var(--gold)"/>
        <path d="M984 385 H1002 M984 391 H1002 M962 401 H1002 M962 407 H992" stroke="var(--slate)" stroke-width="2.5"/>
      </g>
      <!-- mountain with flag -->
      <g class="icon icon-summit">
        <polygon points="1166,420 1197,372 1228,420" fill="var(--slate)"/>
        <polygon points="1188,386 1197,372 1206,386 1200,382 1194,388" fill="#ffffff"/>
        <path d="M1197 372 V356" stroke="var(--charcoal)" stroke-width="2"/>
        <polygon points="1197,356 1210,360 1197,365" fill="var(--gold)"/>
        <rect x="1166" y="418" width="62" height="4" fill="var(--gold)"/>
      </g>
      <!-- rocket -->
      <g class="icon icon-rocket">
        <path d="M1408 360 Q1420 376 1418 404 H1398 Q1396 376 1408 360 Z" fill="#e6e6e6" stroke="var(--charcoal)" stroke-width="2"/>
        <circle cx="1408" cy="384" r="4" fill="var(--gold)"/>
        <polygon points="1398,394 1390,410 1398,406" fill="var(--charcoal)"/>
        <polygon points="1418,394 1426,410 1418,406" fill="var(--charcoal)"/>
        <rect x="1384" y="414" width="48" height="8" rx="4" fill="var(--gold)"/>
      </g>

      <text class="step-label" x="982" y="336">Turn-On the Traffic</text>
      <text class="step-label" x="1199" y="336">Become the Authority</text>
      <text class="step-label" x="1410" y="336">Unlock Your Growth</text>
      <text class="step-label" x="982" y="494">Formulate the Follow-Up</text>
      <text class="step-label" x="1197" y="494">Construct Your Funnel</text>
      <text class="step-label" x="1410" y="494">Develop Lead Generator</text>
      <text class="step-label" x="984" y="663">Clarify the Chaos</text>
      <text class="step-label" x="1197" y="663">Define Your Customer</text>
      <text class="step-label" x="1410" y="663">Master Your Message</text>

      <rect x="726" y="372" width="30" height="34" rx="5" fill="#ffffff" stroke="var(--gold)" stroke-width="3"/>
      <text class="tier-digit" x="741" y="397">3</text>
      <text class="tier-label" x="766" y="391">BREAKTHROUGH</text>
      <path d="M768 398 Q840 394 912 396" stroke="var(--gold)" stroke-width="3" fill="none"/>

      <rect x="726" y="537" width="30" height="34" rx="5" fill="#ffffff" stroke="var(--gold)" stroke-width="3"/>
      <text class="tier-digit" x="741" y="562">2</text>
      <text class="tier-label" x="770" y="556">BUILD</text>
      <path d="M768 563 Q800 560 838 561" stroke="var(--gold)" stroke-width="3" fill="none"/>

      <rect x="726" y="703" width="30" height="34" rx="5" fill="#ffffff" stroke="var(--gold)" stroke-width="3"/>
      <text class="tier-digit" x="741" y="728">1</text>
      <text class="tier-label" x="768" y="722">BLUEPRINT</text>
      <path d="M768 729 Q820 726 870 727" stroke="var(--gold)" stroke-width="3" fill="none"/>

      <text class="endpoint" x="910" y="798">A</text>
      <path d="M930 765 L950 745" stroke="#cfcfcf" stroke-width="2"/>
      <text class="endpoint" x="1494" y="358">B</text>
      <path d="M1448 372 L1486 350 M1486 350 L1474 350 M1486 350 L1482 361" stroke="#cfcfcf" stroke-width="2" fill="none"/>
    </g>
  </svg>

  <header class="brand">
    <div class="brand-square"></div>
    <div class="brand-name">Keystone Ladder<br>Method</div>
  </header>

  <h1 class="headline">A Clear Three Step Roadmap that will finally allow you<br>to attract quality customers and win more jobs.</h1>

  <section class="intro">
    <p>The Keystone Ladder Method is a simple to follow system that was created specifically for Contractors and Blue Collar Business Owners.</p>
    <p>When it comes to marketing and growing their business, the majority of Contractors are left confused, frustrated and extremely overwhelmed. Unlike most sales, marketing &amp; training programs that offer a single "piece of the puzzle", we've mapped out each essential step of the puzzle and cut out all of the fluff.</p>
    <p class="intro-cta">All you have to do is complete each step in the right order and we'll be guiding you along the entire journey!</p>
  </section>

  <ol class="phase-list">
    <li class="phase">
      <span class="phase-number">1</span>
      <h2 class="phase-title">BLUEPRINT:</h2>
      <p class="phase-text">Get clear on where you're going, define your ideal audience, and finally, master your message.</p>
    </li>
    <li class="phase">
      <span class="phase-number">2</span>
      <h2 class="phase-title">BUILD:</h2>
      <p class="phase-text">Attract quality leads, Build your funnel and Formulate a high-converting follow-up system</p>
    </li>
    <li class="phase">
      <span class="phase-number">3</span>
      <h2 class="phase-title">BREAKTHROUGH:</h2>
      <p class="phase-text">Get in front of your ideal customers and rapidly scale your business by driving traffic and becoming the authority in your market</p>
    </li>
  </ol>
</main>
</body>
</html>
```